Cafe Menu for Willow Lantern Cafe

Menu designed for my cafe. I need multiple sizes to be created.
DL pamphlet
A4
and I also need 5 x A3 portraits & 5 x A3 landscapes. The menu must be spread out over a total of 10 A3 pages. I have uploaded my logo which needs to be used & I would like the colours from the logo used. The background of the menu needs to be white. I have uploaded an image on another menu for which I would like the same heading font to be used.

Target Market(s)

cafe, restaurant

Font styles to use
Serif
Decorative
Script

Requirements
Must have
• White back ground
correct font as I have uploaded
Nice to have
• May have drawings of food in back and white.

```html
<!DOCTYPE html>
<html lang="en">
<head>
<meta charset="utf-8">
<title>Willow Lantern Cafe – Menu Set</title>
<link rel="stylesheet" href="https://fonts.googleapis.com/css2?family=Figtree:wght@400;600;700&family=Staatliches&family=Great+Vibes&family=Playfair+Display:wght@600&display=swap">
<style>
:root{
  --board:#333333;
  --paper:#ffffff;
  --leaf:#9aab3d;
  --leaf-deep:#7f922c;
  --leaf-soft:#dfe6c2;
  --ink:#2b2320;
}
*{margin:0;padding:0;box-sizing:border-box}
html,body{width:1200px;height:885px;overflow:hidden;background:var(--board)}
body{position:relative;font-family:'Figtree',sans-serif;color:var(--ink)}
.page{position:absolute;background:var(--paper)}
.portrait{width:224px;height:317px;top:37px}
.landscape{width:321px;height:228px}
.frame{position:absolute;inset:8px;border:1.2px solid var(--leaf)}
.corner{position:absolute;background:var(--leaf-soft);border-radius:3px}
.corner.tl{top:11px;left:11px;width:26px;height:26px}
.corner.tr{top:11px;right:11px;width:26px;height:26px}
.corner.bl{bottom:11px;left:11px;width:15px;height:14px}
.corner.br{bottom:11px;right:11px;width:15px;height:14px}

.brand{position:absolute;left:0;right:0;top:20px;text-align:center}
.brand-name{font-size:7.5px;font-weight:600;color:var(--leaf-deep);letter-spacing:.2px;line-height:9px}
.tagline{font-size:4.4px;line-height:6px}
.brand-dot{display:block;width:5px;height:5px;border-radius:50%;background:var(--leaf);margin:2px auto 2px}
.addr{font-size:2.7px;line-height:3.6px}

.foot{position:absolute;left:0;right:0;bottom:17px;text-align:center;font-size:3.1px;line-height:4.3px}
.foot b{font-size:3.7px;font-weight:700}
.foot .lbl{color:var(--leaf-deep);font-weight:600}
.foot span.v{font-weight:600}

.content{position:absolute}
.section-title{display:flex;align-items:center;gap:6px;font-family:'Staatliches',sans-serif;color:var(--leaf);font-size:12px;line-height:13px;letter-spacing:.6px;margin:9px 0 5px}
.section-title:first-child{margin-top:0}
.sprig{display:inline-block;width:14px;height:5px;background:var(--leaf-soft);border-radius:3px}
.item .row{display:flex;align-items:baseline;font-size:5.9px;font-weight:700;line-height:8.3px}
.item .row .fill{flex:1;border-bottom:0.8px dotted var(--ink);margin:0 2px;transform:translateY(-1.4px)}
.item .row.plain{font-weight:400}
.item .row.plain .price{font-weight:700}
.desc{font-size:5.6px;line-height:8.3px;font-weight:400}

.badge{position:absolute;width:36px;height:36px;border:0.9px solid var(--leaf);border-radius:50%;display:flex;flex-direction:column;align-items:center;justify-content:center;text-align:center;color:var(--leaf-deep);font-weight:700;font-size:2.8px;line-height:3.6px}
.badge svg{margin-bottom:1px}
.ribbon{position:absolute}
.ribbon-label{position:absolute;left:0;right:0;text-align:center;color:#fff}
.script{font-family:'Great Vibes',cursive;font-size:11px;top:1px;line-height:14px}
.menu-info{position:absolute;left:0;right:0;text-align:center;font-family:'Playfair Display',serif;font-size:3.8px}
.menu-info i{display:block;width:26px;height:0.6px;background:var(--ink);margin:1.5px auto 0}
.coffee-banner{font-family:'Playfair Display',serif;font-size:7.4px;letter-spacing:.4px;top:3px;line-height:8px}
.compact .item .row,.compact .desc{line-height:8px}
.compact .section-title{margin:7px 0 4px}
.compact .section-title:first-child{margin-top:0}
</style>
</head>
<body>

<section class="page portrait" style="left:12px">
  <div class="frame"></div>
  <div class="corner tl" role="img" aria-label="Flourish ornament"></div>
  <div class="corner tr" role="img" aria-label="Flourish ornament"></div>
  <div class="corner bl" role="img" aria-label="Flourish ornament"></div>
  <div class="corner br" role="img" aria-label="Flourish ornament"></div>
  <header class="brand" style="top:11px">
    <div class="brand-name">Willow Lantern Cafe</div>
    <div class="tagline">Coffee, breakfast &amp; lunch</div>
    <span class="brand-dot"></span>
    <div class="addr">14 Alder Lane, Fernvale Q<br>Phone: 07 5550 1842</div>
  </header>
  <div class="badge" style="left:35px;top:38px">
    <svg width="7" height="7" viewBox="0 0 10 10"><circle cx="5" cy="5" r="4" fill="none" stroke="#9aab3d" stroke-width="1"/><path d="M5 2.6V5l1.6 1" fill="none" stroke="#9aab3d" stroke-width="1"/></svg>
    Open 7 Days From 7am<br>Open Weekends<br>Saturday &amp; Sunday<br>7am-12pm
  </div>
  <div class="badge" style="left:156px;top:38px;font-size:3.3px;line-height:4.2px">
    <svg width="6" height="8" viewBox="0 0 10 13"><path d="M5 12S1 7.4 1 4.6a4 4 0 0 1 8 0C9 7.4 5 12 5 12z" fill="none" stroke="#9aab3d" stroke-width="1.1"/><circle cx="5" cy="4.6" r="1.4" fill="#9aab3d"/></svg>
    14 Alder<br>Lane,<br>Fernvale Q 4306
  </div>
  <div class="ribbon" style="left:74px;top:55px;width:78px;height:20px">
    <svg width="78" height="20" viewBox="0 0 78 20"><path d="M0 8h10v10H0l4-5z" fill="#7f922c"/><path d="M78 8H68v10h10l-4-5z" fill="#7f922c"/><path d="M8 3q31-4 62 0v13q-31-4-62 0z" fill="#9aab3d"/></svg>
    <div class="ribbon-label script">Main Dishes</div>
  </div>
  <div class="menu-info" style="top:76px">Menu Information<i></i></div>
  <div class="content compact" style="left:33px;top:100px;width:162px">
    <h2 class="section-title"><span class="sprig" role="img" aria-label="Leaf sprig"></span>Cold Drinks</h2>
    <div class="item"><div class="row">Milkshake<span class="fill"></span>$7.00</div></div>
    <div class="item"><div class="row">Thickshake<span class="fill"></span>$8.00</div><p class="desc">Flavours - Chocolate, vanilla, strawberry, banana,<br>caramel &amp; coffee</p></div>
    <div class="item"><div class="row">Iced Latte<span class="fill"></span>$7.50</div><p class="desc">Add syrup: vanilla, caramel, white</p><div class="row plain">chocolate, hazelnut<span class="fill"></span><span class="price">$1.00</span></div></div>
    <div class="item"><div class="row">Iced Coffee<span class="fill"></span>$8.00</div></div>
    <div class="item"><div class="row">Iced Chocolate<span class="fill"></span>$8.00</div></div>
    <div class="item"><div class="row">Iced Mocha<span class="fill"></span>$8.00</div></div>
    <h2 class="section-title"><span class="sprig" role="img" aria-label="Leaf sprig"></span>Juice Bar</h2>
    <div class="item"><div class="row">Passion Pop<span class="fill"></span>$9.00</div><p class="desc">Passionfruit, apple &amp; oranges</p></div>
    <div class="item"><div class="row">Sweet Juice<span class="fill"></span>$9.00</div><p class="desc">Apple, pineapple, oranges &amp; mango</p></div>
    <div class="item"><div class="row">Orange Juice<span class="fill"></span>$9.00</div><p class="desc">Freshly juiced oranges</p></div>
  </div>
  <footer class="foot"><b>Phone Orders Welcome! 07 5550 1842</b><br><span class="lbl">Menu Online:</span> <span class="v">www.willowlanterncafe.com.au</span><br><span class="lbl">Email:</span> <span class="v">hello@willowlanterncafe.com.au</span><br><span class="v">10% Surcharge Applies on Sundays &amp; Public Holidays</span></footer>
</section>

<section class="page portrait" style="left:249px">
  <div class="frame"></div>
  <div class="corner tl" role="img" aria-label="Flourish ornament"></div>
  <div class="corner tr" role="img" aria-label="Flourish ornament"></div>
  <div class="corner bl" role="img" aria-label="Flourish ornament"></div>
  <div class="corner br" role="img" aria-label="Flourish ornament"></div>
  <header class="brand">
    <div class="brand-name">Willow Lantern Cafe</div>
    <div class="tagline">Coffee, breakfast &amp; lunch</div>
    <span class="brand-dot"></span>
    <div class="addr">14 Alder Lane, Fernvale Q<br>Phone: 07 5550 1842</div>
  </header>
  <div class="content" style="left:31px;top:78px;width:160px">
    <h2 class="section-title"><span class="sprig" role="img" aria-label="Leaf sprig"></span>Smoothies</h2>
    <div class="item"><div class="row">Mango Raspberry Smoothie<span class="fill"></span>$9.00</div><p class="desc">Frozen mango &amp; raspberry sorbet blended with coconut milk</p></div>
    <div class="item"><div class="row">Mango Coconut Smoothie<span class="fill"></span>$9.00</div><p class="desc">Frozen mango blended with coconut milk</p></div>
    <div class="item"><div class="row">Berry Blast Smoothie<span class="fill"></span>$9.00</div><p class="desc">Mixed berries blended with coconut milk</p></div>
    <div class="item"><div class="row">Choc Banana Smoothie<span class="fill"></span>$9.00</div><p class="desc">Frozen banana &amp; dark chocolate ice cream blended together with whole milk</p></div>
    <h2 class="section-title"><span class="sprig" role="img" aria-label="Leaf sprig"></span>Frappes</h2>
    <div class="item"><div class="row">Strawberry Lemonade Frappe<span class="fill"></span>$9.00</div><p class="desc">Strawberry syrup blended together with<br>lemonade &amp; ice</p></div>
    <div class="item"><div class="row">Coffee Frappe<span class="fill"></span>$9.00</div><p class="desc">Espresso blended with milk &amp; ice, topped<br>with cream</p></div>
    <div class="item"><div class="row">Chocolate Frappe<span class="fill"></span>$9.00</div><p class="desc">Chocolate syrup blended with milk &amp; ice,<br>topped with cream</p></div>
  </div>
  <footer class="foot"><b>Phone Orders Welcome! 07 5550 1842</b><br><span class="lbl">Menu Online:</span> <span class="v">www.willowlanterncafe.com.au</span><br><span class="lbl">Email:</span> <span class="v">hello@willowlanterncafe.com.au</span><br><span class="v">10% Surcharge Applies on Sundays &amp; Public Holidays</span></footer>
</section>

<section class="page portrait" style="left:486px">
  <div class="frame"></div>
  <div class="corner tl" role="img" aria-label="Flourish ornament"></div>
  <div class="corner tr" role="img" aria-label="Flourish ornament"></div>
  <div class="corner bl" role="img" aria-label="Flourish ornament"></div>
  <div class="corner br" role="img" aria-label="Flourish ornament"></div>
  <header class="brand">
    <div class="brand-name">Willow Lantern Cafe</div>
    <div class="tagline">Coffee, breakfast &amp; lunch</div>
    <span class="brand-dot"></span>
    <div class="addr">14 Alder Lane, Fernvale Q<br>Phone: 07 5550 1842</div>
  </header>
  <div class="ribbon" style="left:61px;top:76px;width:104px;height:16px">
    <svg width="104" height="16" viewBox="0 0 104 16"><path d="M0 3h10v12H0l4-6z" fill="#7f922c"/><path d="M104 3H94v12h10l-4-6z" fill="#7f922c"/><rect x="7" y="1" width="90" height="13" fill="#9aab3d"/><path d="M10 2.4h84" stroke="#dfe6c2" stroke-width=".5"/></svg>
    <div class="ribbon-label coffee-banner">COFFEE MENU</div>
  </div>
  <div class="content" style="left:33px;top:105px;width:152px">
    <h2 class="section-title"><span class="sprig" role="img" aria-label="Leaf sprig"></span>Coffee and Hot Drinks</h2>
    <div class="item"><div class="row">Cappuccino<span class="fill"></span>$4.80</div></div>
    <div class="item"><div class="row">Flat White<span class="fill"></span>$4.80</div></div>
    <div class="item"><div class="row">Latte<span class="fill"></span>$5.00</div></div>
    <div class="item"><div class="row">Long Black<span class="fill"></span>$4.80</div></div>
    <div class="item"><div class="row">Mocha<span class="fill"></span>$5.20</div></div>
    <div class="item"><div class="row">Macchiato<span class="fill"></span>$3.50</div></div>
    <div class="item"><div class="row">Espresso<span class="fill"></span>$3.50</div></div>
    <div class="item"><div class="row">Chai Latte<span class="fill"></span>$4.80</div></div>
    <div class="item"><div class="row">Hot Chocolate<span class="fill"></span>$4.80</div></div>
    <div class="item"><div class="row">Tea<span class="fill"></span>$4.50</div><p class="desc">Tea Flavours: English breakfast, earl grey, green, berry green &amp; coconut</p></div>
    <h2 class="section-title" style="margin-top:11px"><span class="sprig" role="img" aria-label="Leaf sprig"></span>Takeway Coffee</h2>
    <div class="item"><div class="row">Takeaway Large<span class="fill"></span>$6.80</div></div>
    <div class="item"><div class="row">Regular<span class="fill"></span>$5.20</div></div>
    <div class="item"><div class="row">Takeaway Small<span class="fill"></span>$4.80</div></div>
  </div>
  <footer class="foot"><b>Phone Orders Welcome! 07 5550 1842</b><br><span class="lbl">Menu Online:</span> <span class="v">www.willowlanterncafe.com.au</span><br><span class="lbl">Email:</span> <span class="v">hello@willowlanterncafe.com.au</span><br><span class="v">10% Surcharge Applies on Sundays &amp; Public Holidays</span></footer>
</section>

<section class="page portrait" style="left:723px">
  <div class="frame"></div>
  <div class="corner tl" role="img" aria-label="Flourish ornament"></div>
  <div class="corner tr" role="img" aria-label="Flourish ornament"></div>
  <div class="corner bl" role="img" aria-label="Flourish ornament"></div>
  <div class="corner br" role="img" aria-label="Flourish ornament"></div>
  <header class="brand">
    <div class="brand-name">Willow Lantern Cafe</div>
    <div class="tagline">Coffee, breakfast &amp; lunch</div>
    <span class="brand-dot"></span>
    <div class="addr">14 Alder Lane, Fernvale Q<br>Phone: 07 5550 1842</div>
  </header>
  <div class="content" style="left:32px;top:98px;width:160px">
    <h2 class="section-title"><span class="sprig" role="img" aria-label="Leaf sprig"></span>Coffee Extras</h2>
    <div class="item"><div class="row">Mug &amp; Extra Shot 50c</div></div>
    <div class="item"><div class="row">Soy &amp; Lactose Free Milk 80c</div></div>
    <div class="item"><div class="row">Syrups<span class="fill"></span>$1.00</div><p class="desc">Flavours - Vanilla, caramel, hazelnut &amp; white<br>chocolate</p></div>
    <h2 class="section-title" style="margin-top:11px"><span class="sprig" role="img" aria-label="Leaf sprig"></span>Kids Menu</h2>
    <div class="item"><div class="row">Scrambled Eggs<span class="fill"></span>$9.50</div><p class="desc">&nbsp;Two eggs scrambled with toast &amp; tomato sauce</p></div>
    <div class="item"><div class="row">Rainbow Pancakes<span class="fill"></span>$9.50</div><p class="desc">&nbsp;Two small pancakes served with ice cream &amp; sprinkles</p></div>
    <div class="item"><div class="row">Nuggets &amp; Chips<span class="fill"></span>$8.00</div></div>
    <div class="item"><div class="row">Chicken Chippees<span class="fill"></span>$8.50</div></div>
  </div>
  <footer class="foot"><b>Phone Orders Welcome! 07 5550 1842</b><br><span class="lbl">Menu Online:</span> <span class="v">www.willowlanterncafe.com.au</span><br><span class="lbl">Email:</span> <span class="v">hello@willowlanterncafe.com.au</span><br><span class="v">10% Surcharge Applies on Sundays &amp; Public Holidays</span></footer>
</section>

<section class="page portrait" style="left:962px">
  <div class="frame"></div>
  <div class="corner tl" role="img" aria-label="Flourish ornament"></div>
  <div class="corner tr" role="img" aria-label="Flourish ornament"></div>
  <div class="corner bl" role="img" aria-label="Flourish ornament"></div>
  <div class="corner br" role="img" aria-label="Flourish ornament"></div>
  <header class="brand">
    <div class="brand-name">Willow Lantern Cafe</div>
    <div class="tagline">Coffee, breakfast &amp; lunch</div>
    <span class="brand-dot"></span>
    <div class="addr">14 Alder Lane, Fernvale Q<br>Phone: 07 5550 1842</div>
  </header>
  <div class="content" style="left:31px;top:80px;width:164px">
    <h2 class="section-title"><span class="sprig" role="img" aria-label="Leaf sprig"></span>Breakfast Menu</h2>
    <div class="item"><div class="row">Big Breakfast<span class="fill"></span>$21.50</div><p class="desc">Bacon, sausages, hash browns, tomato, baked beans &amp; mushrooms with a slice of toasted sourdough bread &amp; your choice of fried, poached or scrambled eggs</p></div>
    <div class="item"><div class="row">Classic Breakfast<span class="fill"></span>$16.50</div><p class="desc">Your choice of fried poached or scrambled eggs served with either bacon or sausages, tomato &amp; a slice of toasted sour-dough bread</p></div>
    <div class="item"><div class="row">Avocado Stack<span class="fill"></span>$17.00</div><p class="desc">Turkish bread topped with smashed avocado, bacon or salmon, 2 poached eggs &amp; a sprinkle of feta cheese</p></div>
    <div class="item"><div class="row">Eggs Benedict<span class="fill"></span>$19.00</div><p class="desc">Your choice of bacon, ham or salmon served with toasted turkish bread, poached eggs &amp; creamy hollandaise sauce</p></div>
    <div class="item"><div class="row">Classic Omelet<span class="fill"></span>$17.50</div><p class="desc">Ham, tomato, spinach, onion &amp; cheese omelet topped with fried cherry tomatoes &amp; turkish toast</p></div>
    <div class="item"><div class="row">Panini Scramble<span class="fill"></span>$16.50</div><p class="desc">Toasted panini bread topped with scrambled eggs, sautéed mushrooms, cherry tomatoes &amp; spinach with a drizzle of hollandaise sauce on top</p></div>
  </div>
  <footer class="foot"><b>Phone Orders Welcome! 07 5550 1842</b><br><span class="lbl">Menu Online:</span> <span class="v">www.willowlanterncafe.com.au</span><br><span class="lbl">Email:</span> <span class="v">hello@willowlanterncafe.com.au</span><br><span class="v">10% Surcharge Applies on Sundays &amp; Public Holidays</span></footer>
</section>

<section class="page landscape" style="left:104px;top:374px">
  <div class="frame"></div>
  <div class="corner tl" role="img" aria-label="Flourish ornament"></div>
  <div class="corner tr" role="img" aria-label="Flourish ornament"></div>
  <div class="corner bl" role="img" aria-label="Flourish ornament"></div>
  <div class="corner br" role="img" aria-label="Flourish ornament"></div>
  <header class="brand" style="top:14px">
    <div class="brand-name">Willow Lantern Cafe</div>
    <div class="tagline">Coffee, breakfast &amp; lunch</div>
    <span class="brand-dot"></span>
    <div class="addr">14 Alder Lane, Fernvale Q<br>Phone: 07 5550 1842</div>
  </header>
  <div class="content" style="left:22px;top:59px;width:277px">
    <div class="item"><div class="row">Breaky Wrap<span class="fill"></span>$15.00</div><p class="desc">Bacon, eggs, hash browns, cheese &amp; BBQ sauce on a toasted wrap</p></div>
    <div class="item"><div class="row">Ultimate Breakfast Toastie<span class="fill"></span>$14.50</div><p class="desc">Bacon, scrambled eggs, smashed avocado, spinach &amp; feta with hollandaise sauce on a toasted ciabat-ta sandwich roll</p></div>
    <div class="item"><div class="row">Breakfast Share Plate<span class="fill"></span>$32.50</div><p class="desc">A delicious selection of yummy breakfast items including bacon, scrambled eggs, hash browns,</p></div>
    <h2 class="section-title" style="margin:5px 0 2px"><span class="sprig" role="img" aria-label="Leaf sprig"></span>Lunch</h2>
    <div class="item"><div class="row">Parmi Turkish Roll<span class="fill"></span>$16.50</div><p class="desc">Chicken tenders, tomato relish, cheese, lettuce &amp; herb mayo served on a toasted turkish roll with a side of chips</p></div>
    <div class="item"><div class="row">Sweet Potato Chips<span class="fill"></span>$13.50</div><p class="desc">Seasoned sweet potato chips served with a herb mayonnaise</p></div>
    <div class="item"><div class="row">Chicken Avocado Panini Grill<span class="fill"></span>$15.50</div><p class="desc">Chicken, smashed avocado, cheese &amp; aioli served on toasted panini bread &amp; grilled with a side of chips</p></div>
  </div>
  <footer class="foot" style="bottom:13px"><b>Phone Orders Welcome! 07 5550 1842</b><br><span class="lbl">Menu Online:</span> <span class="v">www.willowlanterncafe.com.au</span><br><span class="lbl">Email:</span> <span class="v">hello@willowlanterncafe.com.au</span><br><span class="v">10% Surcharge Applies on Sundays &amp; Public Holidays</span></footer>
</section>

<section class="page landscape" style="left:442px;top:374px">
  <div class="frame"></div>
  <div class="corner tl" role="img" aria-label="Flourish ornament"></div>
  <div class="corner tr" role="img" aria-label="Flourish ornament"></div>
  <div class="corner bl" role="img" aria-label="Flourish ornament"></div>
  <div class="corner br" role="img" aria-label="Flourish ornament"></div>
  <header class="brand" style="top:14px">
    <div class="brand-name">Willow Lantern Cafe</div>
    <div class="tagline">Coffee, breakfast &amp; lunch</div>
    <span class="brand-dot"></span>
    <div class="addr">14 Alder Lane, Fernvale Q<br>Phone: 07 5550 1842</div>
  </header>
  <div class="content" style="left:21px;top:66px;width:275px">
    <div class="item"><div class="row">Steak Sandwich<span class="fill"></span>$17.50</div><p class="desc">Fillet steak with salad, cheese &amp; BBQ sauce on toasted bread with a side of chips</p></div>
    <div class="item"><div class="row">Club Sandwich<span class="fill"></span>$16.50</div><p class="desc">Three slices of toasted bread with ham, bacon, chicken, tomato,cheese, lettuce &amp; mayonnaise with a side of chips</p></div>
    <div class="item"><div class="row">Fresh or Toasted Sandwich<span class="fill"></span>$8.00</div><p class="desc">Your choice of meat, salad &amp; sauce on fresh white or wholemeal bread toasted or fresh</p></div>
    <div class="item"><div class="row">Pulled Pork Turkish Roll<span class="fill"></span>$15.50</div><p class="desc">Pulled pork mixed with gravy, house made coleslaw, lettuce &amp; herb mayonnaise on a toasted turkish roll with a side of chips</p></div>
    <div class="item"><div class="row">Fish, Chips &amp; Salad<span class="fill"></span>$17.50</div><p class="desc">Battered fillets with chips &amp; salad, herb mayonnaise, lemon &amp; salad dressing.</p></div>
    <div class="item"><div class="row">Nachos<span class="fill"></span>$16.50</div><p class="desc">Nacho chips topped with nacho mince, cheese sauce, melted cheese, diced tomato &amp; smashed avocado.</p></div>
  </div>
  <footer class="foot" style="bottom:13px"><b>Phone Orders Welcome! 07 5550 1842</b><br><span class="lbl">Menu Online:</span> <span class="v">www.willowlanterncafe.com.au</span><br><span class="lbl">Email:</span> <span class="v">hello@willowlanterncafe.com.au</span><br><span class="v">10% Surcharge Applies on Sundays &amp; Public Holidays</span></footer>
</section>

<section class="page landscape" style="left:778px;top:374px">
  <div class="frame"></div>
  <div class="corner tl" role="img" aria-label="Flourish ornament"></div>
  <div class="corner tr" role="img" aria-label="Flourish ornament"></div>
  <div class="corner bl" role="img" aria-label="Flourish ornament"></div>
  <div class="corner br" role="img" aria-label="Flourish ornament"></div>
  <header class="brand" style="top:14px">
    <div class="brand-name">Willow Lantern Cafe</div>
    <div class="tagline">Coffee, breakfast &amp; lunch</div>
    <span class="brand-dot"></span>
    <div class="addr">14 Alder Lane, Fernvale Q<br>Phone: 07 5550 1842</div>
  </header>
  <div class="content" style="left:20px;top:70px;width:275px">
    <div class="item"><div class="row">Lunch Bruschetta<span class="fill"></span>$16.50</div><p class="desc">Toasted sourdough bread with avocado, cherry tomatoes, onion, feta &amp; a drizzle of balsamic glaze with a side of chips</p></div>
    <div class="item"><div class="row">Karaage Chicken<span class="fill"></span>$16.50</div><p class="desc">Delicious crispy karaage chicken on top of a bed of white rice with avocado Japanese silken mayonnaise &amp; teriyaki sauce</p></div>
    <h2 class="section-title" style="margin:9px 0 3px;font-size:14px"><span class="sprig" role="img" aria-label="Leaf sprig"></span>Salads</h2>
    <div class="item"><div class="row">Caesar Salad<span class="fill"></span>$16.50</div><p class="desc">Chicken breast with lettuce, bacon, egg, parmesan cheese, croutons &amp; caesar dressing</p></div>
    <div class="item"><div class="row">Mango Chicken Salad<span class="fill"></span>$16.50</div><p class="desc">Chicken breast with lettuce, mango, onion &amp; cashews with a creamy tangy curry dressing</p></div>
  </div>
  <footer class="foot" style="bottom:13px"><b>Phone Orders Welcome! 07 5550 1842</b><br><span class="lbl">Menu Online:</span> <span class="v">www.willowlanterncafe.com.au</span><br><span class="lbl">Email:</span> <span class="v">hello@willowlanterncafe.com.au</span><br><span class="v">10% Surcharge Applies on Sundays &amp; Public Holidays</span></footer>
</section>

<section class="page landscape" style="left:277px;top:620px">
  <div class="frame"></div>
  <div class="corner tl" role="img" aria-label="Flourish ornament"></div>
  <div class="corner tr" role="img" aria-label="Flourish ornament"></div>
  <div class="corner bl" role="img" aria-label="Flourish ornament"></div>
  <div class="corner br" role="img" aria-label="Flourish ornament"></div>
  <header class="brand" style="top:14px">
    <div class="brand-name">Willow Lantern Cafe</div>
    <div class="tagline">Coffee, breakfast &amp; lunch</div>
    <span class="brand-dot"></span>
    <div class="addr">14 Alder Lane, Fernvale Q<br>Phone: 07 5550 1842</div>
  </header>
  <div class="content" style="left:20px;top:68px;width:277px">
    <div class="item"><div class="row">Tropical Prawn Salad<span class="fill"></span>$17.50</div><p class="desc">Cooked prawns with avocado, tomato, cucumber and mango salsa mixed through with lettuce and a sweet poppyseed dressing</p></div>
    <h2 class="section-title" style="margin:8px 0 3px;font-size:14px"><span class="sprig" role="img" aria-label="Leaf sprig"></span>Burger</h2>
    <div class="item"><div class="row">The Roadhouse Burger<span class="fill"></span>$17.50</div><p class="desc">Mince patty, double burger cheese, tomato, lettuce &amp; onion with a hot sriracha mayonnaise served with chips</p></div>
    <div class="item"><div class="row">The Fiery Burger<span class="fill"></span>$18.50</div><p class="desc">Mince patty, double burger cheese, tomato &amp; onion with a hot sriracha mayonnaise served with chips</p></div>
    <div class="item"><div class="row">Barramundi Burger<span class="fill"></span>$16.50</div><p class="desc">Crispy barramundi fillet with lettuce, tomato, onion, cheese &amp; tartare sauce on a toasted herb focaccia roll served with chips</p></div>
  </div>
  <footer class="foot" style="bottom:13px"><b>Phone Orders Welcome! 07 5550 1842</b><br><span class="lbl">Menu Online:</span> <span class="v">www.willowlanterncafe.com.au</span><br><span class="lbl">Email:</span> <span class="v">hello@willowlanterncafe.com.au</span><br><span class="v">10% Surcharge Applies on Sundays &amp; Public Holidays</span></footer>
</section>

<section class="page landscape" style="left:617px;top:620px">
  <div class="frame"></div>
  <div class="corner tl" role="img" aria-label="Flourish ornament"></div>
  <div class="corner tr" role="img" aria-label="Flourish ornament"></div>
  <div class="corner bl" role="img" aria-label="Flourish ornament"></div>
  <div class="corner br" role="img" aria-label="Flourish ornament"></div>
  <header class="brand" style="top:14px">
    <div class="brand-name">Willow Lantern Cafe</div>
    <div class="tagline">Coffee, breakfast &amp; lunch</div>
    <span class="brand-dot"></span>
    <div class="addr">14 Alder Lane, Fernvale Q<br>Phone: 07 5550 1842</div>
  </header>
  <div class="content" style="left:28px;top:73px;width:263px">
    <div class="item"><div class="row">Beef Burger<span class="fill"></span>$15.50</div><p class="desc">Steak or mince with salad, cheese &amp; BBQ sauce with a side of chips</p><div class="row">Add Bacon $2.00 ~ Add Egg $2.00</div></div>
    <div class="item"><div class="row">Ultimate Chicken Burger<span class="fill"></span>$17.00</div><p class="desc">Southern style chicken patty with bacon, pineapple, salad, cheese &amp; mayonnaise with a side of chips</p></div>
    <div class="item"><div class="row">Chicken Avocado Burger<span class="fill"></span>$17.00</div><p class="desc">Southern style chicken patty with bacon, avocado, lettuce, tomato, cheese &amp; mayonnaise with a side of chips</p></div>
    <div class="item"><div class="row">Herb Chicken Burger<span class="fill"></span>$17.00</div><p class="desc">Southern style chicken patty with bacon, smashed avocado, cheese, lettuce, tomato, onion, tomato relish &amp; a delicious homemade herb mayonnaise with a side of chips</p></div>
  </div>
  <footer class="foot" style="bottom:13px"><b>Phone Orders Welcome! 07 5550 1842</b><br><span class="lbl">Menu Online:</span> <span class="v">www.willowlanterncafe.com.au</span><br><span class="lbl">Email:</span> <span class="v">hello@willowlanterncafe.com.au</span><br><span class="v">10% Surcharge Applies on Sundays &amp; Public Holidays</span></footer>
</section>

</body>
</html>
```